Copperleaf Motorized Shade Business Card

Hello, we've had our logo made. Now we are looking for a clean and cool looking business card. One side can just be the logo with any design elements that might look good with it. The other side will be Name, Phone Number and Email. There will not be an address on the card.

```html
<!DOCTYPE html>
<html lang="en">
<head>
<meta charset="utf-8">
<title>Copperleaf Motorized Shade – Business Card</title>
<link href="https://fonts.googleapis.com/css2?family=Oswald:wght@500;600&family=Open+Sans:wght@300;400;700&display=swap" rel="stylesheet">
<style>
  :root {
    --bg: #1c1b1d;
    --paper: #f3f3f1;
    --navy: #0f3a78;
    --navy-deep: #173769;
    --navy-light: #234f8f;
    --sky: #2aa6dc;
    --gold: #eab21c;
    --ink: #4a4a4a;
    --rule: #9a9a9a;
  }
  * { box-sizing: border-box; margin: 0; padding: 0; }
  html, body {
    width: 842px; height: 1200px; overflow: hidden;
    background: var(--bg);
  }
  .sheet {
    width: 842px; height: 1200px;
    display: flex; flex-direction: column; align-items: center; justify-content: center;
    gap: 120px;
  }
  .card {
    position: relative;
    width: 700px; height: 400px;
    border-radius: 26px;
    overflow: hidden;
  }
  /* Front */
  .card--front { background: var(--paper); }
  .card__wave { position: absolute; inset: 0; width: 100%; height: 100%; }
  .brand {
    position: absolute; left: 40px; top: 158px;
    display: flex; align-items: center; gap: 14px;
  }
  .brand__mark { width: 22px; height: 22px; background: var(--gold); flex: none; }
  .brand__name {
    font-family: "Oswald", sans-serif; font-weight: 600;
    font-size: 25px; letter-spacing: 0.5px; text-transform: uppercase;
    color: var(--navy); line-height: 1.15; width: 190px;
  }
  .divider {
    position: absolute; left: 270px; top: 112px;
    width: 1px; height: 104px; background: var(--rule);
  }
  .contact { position: absolute; left: 298px; top: 92px; }
  .contact__name {
    font-family: "Oswald", sans-serif; font-weight: 600;
    font-size: 34px; color: var(--navy); letter-spacing: 0.5px;
    text-transform: uppercase; line-height: 1.1; margin-bottom: 12px;
  }
  .contact__line {
    display: flex; align-items: center; gap: 10px;
    font-family: "Open Sans", sans-serif; font-weight: 300;
    font-size: 16px; color: var(--ink); line-height: 1.75;
    white-space: nowrap;
  }
  .contact__icon { width: 14px; height: 14px; flex: none; }
  /* Back */
  .card--back {
    background: linear-gradient(135deg, var(--navy-deep) 0%, var(--navy) 55%, var(--navy-light) 100%);
  }
  .card__decor {
    position: absolute; right: 40px; top: 40px; width: 420px; height: 320px;
    border-radius: 160px 40px 40px 40px;
    background: radial-gradient(ellipse at 60% 35%, rgba(120,150,200,0.35), rgba(120,150,200,0.08) 70%, transparent);
  }
  .card__gloss {
    position: absolute; inset: 0;
    background: linear-gradient(115deg, transparent 35%, rgba(255,255,255,0.07) 45%, transparent 60%);
  }
  .web {
    position: absolute; left: 44px; top: 36px;
    font-family: "Open Sans", sans-serif; font-size: 18px; color: #e6ecf5; font-weight: 300;
  }
  .web__domain { color: var(--gold); font-weight: 700; }
  .brand--back { left: 210px; top: 268px; }
  .brand--back .brand__name { color: #ffffff; width: auto; }
</style>
</head>
<body>
<main class="sheet">

  <section class="card card--front" aria-label="Business card front">
    <svg class="card__wave" viewBox="0 0 700 400" preserveAspectRatio="none" aria-hidden="true">
      <path d="M0,400 L0,392 C300,390 520,370 580,230 C620,120 650,45 700,32 L700,400 Z" fill="var(--navy)"/>
      <path d="M0,385 C300,383 514,363 574,226" fill="none" stroke="var(--sky)" stroke-width="5"/>
      <path d="M574,226 C614,114 646,36 700,24" fill="none" stroke="var(--gold)" stroke-width="6"/>
    </svg>

    <div class="brand">
      <span class="brand__mark" aria-hidden="true"></span>
      <span class="brand__name">Copperleaf Motorized Shade</span>
    </div>

    <div class="divider" aria-hidden="true"></div>

    <div class="contact">
      <p class="contact__name">Marcus Ellery</p>
      <p class="contact__line">
        <svg class="contact__icon" viewBox="0 0 16 16" aria-hidden="true"><circle cx="8" cy="8" r="8" fill="var(--sky)"/><path d="M5 4.5c0 3.5 3 6.5 6.5 6.5l.7-1.6-1.8-.8-.8.9C8 8.7 7.3 8 6.5 6.4l.9-.8-.8-1.8z" fill="#fff"/></svg>
        310.555.0142
      </p>
      <p class="contact__line">
        <svg class="contact__icon" viewBox="0 0 16 12" aria-hidden="true"><rect width="16" height="12" rx="1" fill="var(--sky)"/><path d="M1 1l7 6 7-6" fill="none" stroke="#fff" stroke-width="1.4"/></svg>
        info@copperleafmotorized.com
      </p>
    </div>
  </section>

  <section class="card card--back" aria-label="Business card back">
    <div class="card__decor" role="img" aria-label="Large faint shade graphic in soft blue"></div>
    <div class="card__gloss" aria-hidden="true"></div>
    <p class="web"><span class="web__domain">copperleafmotorized</span>.com</p>
    <div class="brand brand--back">
      <span class="brand__mark" aria-hidden="true"></span>
      <span class="brand__name">Copperleaf Motorized Shade</span>
    </div>
  </section>

</main>
</body>
</html>
```